Bi-Lingual Trash and Recycle Sign

Hello,

Pretty straight forward. I have not been able to find the exact sign we need for a property with trash and recycle guidelines. I've found close, but not complete. We are looking to have metal 12x18 street sign type signs made to provide these instructions. Attached is a sample taken from the web. I want to be sure to avoid conflicting with them so looking for the same wording but in our own. I'd also like to include our company logo, also attached in vector in horizontal and vertical for inclusion.

```html
<!DOCTYPE html>
<html lang="en">
<head>
<meta charset="UTF-8">
<title>Recycle / Reciclar – Property Sign</title>
<link href="https://fonts.googleapis.com/css2?family=Poppins:wght@500;600;700;800&display=swap" rel="stylesheet">
<style>
  :root {
    --page-bg: #e9ebea;
    --sign-edge: #f7f8f8;
    --frame-black: #151716;
    --green-light: #3f9a6a;
    --green-dark: #12653f;
    --panel-light: #f1f2f2;
    --panel-mid: #dfe2e1;
    --alert-red: #d8262c;
    --ink: #161616;
    --brand: #3a1f2b;
    --white: #ffffff;
  }
  * { margin: 0; padding: 0; box-sizing: border-box; }
  html, body {
    width: 1200px; height: 1200px; overflow: hidden;
    background: var(--page-bg);
    font-family: "Poppins", sans-serif;
  }
  .sign {
    position: absolute; left: 225px; top: 18px;
    width: 750px; height: 1164px;
    background: var(--sign-edge);
    border-radius: 22px;
    box-shadow: 0 0 0 1px #cfd3d2;
  }
  .sign-frame {
    position: absolute; left: 12px; top: 22px; right: 10px; bottom: 20px;
    border: 9px solid var(--frame-black);
    border-radius: 26px;
    background: linear-gradient(180deg, var(--panel-mid) 0%, var(--panel-light) 45%, var(--panel-mid) 100%);
    overflow: hidden;
  }
  .sign-header {
    position: absolute; left: 0; right: 0; top: 0; height: 198px;
    background: linear-gradient(90deg, var(--green-light), var(--green-dark));
    color: var(--white); text-align: center;
  }
  .title {
    position: absolute; left: 0; right: 0;
    font-weight: 800; font-size: 78px; line-height: 1; letter-spacing: 1px;
  }
  .title-en { top: 22px; }
  .title-es { top: 118px; }
  .title-rule {
    position: absolute; left: 50%; top: 98px; width: 390px; height: 6px;
    margin-left: -195px; background: var(--white);
  }
  .line {
    position: absolute; left: 0; right: 0; text-align: center; line-height: 1.3;
  }
  .alert { color: var(--alert-red); font-weight: 700; font-size: 31px; letter-spacing: -0.3px; }
  .icon { position: absolute; left: 50%; }
  .icon-nobag { top: 191px; width: 108px; height: 108px; margin-left: -67px; }
  .icon-recycle { top: 403px; width: 84px; height: 84px; margin-left: -55px; }
  .stream { color: var(--ink); font-weight: 700; font-size: 26px; letter-spacing: -0.3px; }
  .accepted {
    position: absolute; left: 32px; right: 32px; top: 592px; height: 236px;
    border: 3px solid var(--green-dark); border-top: none;
    border-radius: 0 0 16px 16px;
    background: var(--panel-light);
  }
  .accepted-head {
    height: 66px; margin: 0 -3px;
    background: var(--green-dark); color: var(--white);
    font-weight: 700; font-size: 25px; text-align: center; line-height: 66px;
  }
  .accepted-list {
    list-style: none; text-align: center; padding-top: 4px;
    color: var(--ink); font-weight: 600; font-size: 19px; line-height: 31.5px;
  }
  .accepted-list li::before {
    content: ""; display: inline-block; width: 10px; height: 10px;
    background: var(--green-dark); margin-right: 8px; vertical-align: 1px;
  }
  .accepted-list .plain::before { display: none; }
  .brand { position: absolute; left: 0; right: 0; top: 980px; text-align: center; }
  .brand-mark {
    display: block; width: 30px; height: 30px; margin: 0 auto 14px;
    background: var(--brand);
  }
  .brand-name { color: var(--brand); font-weight: 600; font-size: 30px; letter-spacing: 1px; }
</style>
</head>
<body>
  <div class="sign">
    <div class="sign-frame">
      <header class="sign-header">
        <div class="title title-en">RECYCLE</div>
        <div class="title-rule"></div>
        <div class="title title-es">RECICLAR</div>
      </header>

      <svg class="icon icon-nobag" viewBox="0 0 108 108" aria-label="No plastic bags">
        <circle cx="54" cy="54" r="49" fill="#fff" stroke="#d8262c" stroke-width="7"/>
        <path d="M36 40 h8 c0 -10 4 -14 10 -14 s10 4 10 14 h8 l-2 40 h-32 z M48 40 h12 c0-6 -2-9 -6-9 s-6 3 -6 9z" fill="#151716" fill-rule="evenodd"/>
        <line x1="20" y1="22" x2="88" y2="86" stroke="#d8262c" stroke-width="7"/>
      </svg>

      <div class="line alert" style="top:306px">NO PLASTIC BAGS / NO SE ACEPTAN</div>
      <div class="line alert" style="top:348px">BOLSAS PLÁSTICAS</div>

      <svg class="icon icon-recycle" viewBox="0 0 84 84" aria-label="Recycling symbol">
        <g fill="none" stroke="#2f8c5a" stroke-width="9" stroke-linejoin="round">
          <path d="M30 18 L22 32"/>
          <path d="M52 18 L62 34"/>
          <path d="M66 50 L58 66 H44"/>
          <path d="M28 66 H18 L12 54"/>
        </g>
        <g fill="#2f8c5a">
          <polygon points="34,10 50,10 58,24 46,24"/>
          <polygon points="54,36 70,32 74,50 62,46"/>
          <polygon points="38,58 38,76 26,66"/>
          <polygon points="8,42 24,40 16,58"/>
        </g>
      </svg>

      <div class="line stream" style="top:486px">Single-Stream Recycling /</div>
      <div class="line stream" style="top:521px">/ Reciclaje de Flujo Único</div>

      <section class="accepted">
        <div class="accepted-head">Accepted Items / Materiales Aceptados:</div>
        <ul class="accepted-list">
          <li>Glass, Tin, Aluminum / Vidrio, Hojalata, Aluminio</li>
          <li>Plastics (#1-7) / Plásticos (#1-7)</li>
          <li>Cardboard / Cartón</li>
          <li>Mixed Paper, Newspapers, Magazines / Papel Mixto,</li>
          <li class="plain">Periódicos, Revistas</li>
        </ul>
      </section>

      <div class="line alert" style="top:848px">DO NOT INCLUDE TRASH /</div>
      <div class="line alert" style="top:886px">NO INCLUIR BASURA</div>

      <div class="brand">
        <span class="brand-mark"></span>
        <span class="brand-name">HALVERN PROPERTIES</span>
      </div>
    </div>
  </div>
</body>
</html>
```